Propose a revamped landing page

One template we like eg is https://www.trovask.com but but cluttered Our logo and colors are attached to our logo and colors are printed on a white background what we have. So font usage ...
1 page

```html
<!DOCTYPE html>
<html lang="en">
<head>
<meta charset="utf-8">
<title>Voltwise – Always switch to the cheapest energy provider</title>
<link rel="stylesheet" href="https://fonts.googleapis.com/css2?family=Open+Sans:wght@300;400;600;700;800&display=swap">
<style>
:root{
  --slate:#4a5660;
  --slate-dark:#3d4750;
  --amber:#f6a623;
  --orange:#f4601e;
  --cream:#fdebc8;
  --ink:#3b4650;
  --text:#5b636b;
  --muted:#e9ebee;
  --white:#ffffff;
}
*{margin:0;padding:0;box-sizing:border-box}
html,body{width:1200px;height:2731px;overflow:hidden}
body{position:relative;background:var(--white);font-family:'Open Sans',Arial,sans-serif;color:var(--text)}
.abs{position:absolute}
.hero-bg{left:0;top:0;width:1200px;height:520px}
.brand-tag{left:113px;top:0;width:133px;height:128px}
.brand-tag .name{position:absolute;left:0;top:18px;width:133px;text-align:center;font-weight:800;font-size:26px;line-height:26px;color:var(--amber)}
.brand-tag .tagline{position:absolute;left:14px;top:52px;width:105px;text-align:center;font-size:7px;line-height:9px;color:var(--ink)}
.social{display:flex;gap:8px}
.social span{width:22px;height:22px;border:1.5px solid var(--white);border-radius:50%;display:block}
.social.dark span{border-color:var(--ink)}
.header-social{left:973px;top:22px}
.nav{left:586px;top:62px;display:flex;gap:32px;font-size:10px;font-weight:700;color:var(--white);letter-spacing:.2px}
.hero-brand{left:116px;top:170px;display:flex;align-items:center;gap:12px}
.hero-brand .name{font-weight:800;font-size:44px;color:var(--amber);line-height:1}
.hero-brand .dot{width:34px;height:34px;border-radius:50%;background:var(--white)}
.hero-title{left:116px;top:266px;width:440px;font-weight:800;font-size:33px;line-height:38px;color:var(--white)}
.btn{display:inline-block;background:var(--amber);color:var(--white);font-weight:700;font-size:11px;border-radius:22px;text-align:center;letter-spacing:.3px}
.hero-btn{left:118px;top:403px;width:138px;height:42px;line-height:42px}
.hero-disc{left:548px;top:80px;width:560px;height:560px}
.section-title{left:0;width:1200px;text-align:center}
.known{top:678px;font-weight:800;font-size:34px;color:var(--amber)}
.press{left:200px;top:766px;width:800px;height:40px}
.press .arrow{position:absolute;top:6px;width:16px;height:28px}
.press .badge{position:absolute;top:10px;height:20px;background:#d5d9dd;border-radius:3px}
.how{top:870px;font-weight:300;font-size:37px;color:var(--ink)}
.how b{font-weight:800;color:var(--amber)}
.step-num{font-weight:800;font-size:90px;color:var(--muted);line-height:1}
.card{background:var(--white);border-radius:8px;box-shadow:0 6px 22px rgba(0,0,0,.10)}
.step{width:224px;height:140px;padding:30px 20px 0}
.step h3{font-weight:700;font-size:18px;color:var(--amber);line-height:21px;margin-bottom:12px}
.step p{font-size:10px;line-height:15px;color:var(--text)}
.portrait{left:0;top:1245px;width:480px;height:380px}
.feature-title{left:546px;top:1288px;width:460px;font-weight:800;font-size:36px;line-height:38px;color:var(--ink)}
.feature-lead{left:548px;top:1384px;width:420px;font-size:15px;line-height:24px;color:var(--ink)}
.feature-body{left:548px;top:1448px;width:400px;font-size:11px;line-height:19px}
.feature-body p{margin-bottom:14px}
.feature-btn{left:548px;top:1565px;width:138px;height:44px;line-height:44px}
.offer-bg{left:0;top:1690px;width:1200px;height:1041px}
.offer-title{left:248px;top:1796px;width:420px;font-weight:800;font-size:35px;line-height:40px;color:var(--white)}
.offer-sub{left:250px;top:1892px;font-weight:700;font-size:17px;color:var(--cream)}
.offer-list{left:250px;top:1938px;list-style:none;font-size:10px;color:var(--white)}
.offer-list li{position:relative;padding-left:26px;height:36px;line-height:14px}
.offer-list li::before{content:"»";position:absolute;left:0;top:-2px;font-size:15px;color:var(--cream)}
.offer-btn{left:250px;top:2092px;width:138px;height:42px;line-height:42px}
.device{left:686px;top:1808px;width:236px;height:476px;border-radius:36px;background:linear-gradient(160deg,#f3f3f3,#dcd6cc)}
.save{top:2334px;font-weight:300;font-size:36px;color:var(--ink)}
.save b{font-weight:800;color:var(--orange)}
.value{width:222px;height:162px;padding:60px 20px 0}
.value h3{font-weight:800;font-size:18px;color:var(--ink);margin-bottom:10px}
.value p{font-size:10px;line-height:15px}
.value-icon{width:62px;height:50px;border-radius:6px;background:var(--amber)}
.footer-brand{left:249px;top:2660px}
.footer-brand .name{font-weight:800;font-size:30px;color:var(--amber);line-height:1}
.footer-brand .tagline{font-size:6px;color:var(--ink);margin-top:3px}
.footer-social{left:848px;top:2650px}
.footer-links{left:686px;top:2687px;font-size:10px;font-weight:700;color:var(--ink);letter-spacing:.3px}
.footer-links span{margin:0 12px}
</style>
</head>
<body>

<svg class="abs hero-bg" viewBox="0 0 1200 520" aria-hidden="true">
  <path d="M0 0H1200V330C1080 420 900 470 720 468C460 466 200 460 0 495Z" fill="var(--slate)"/>
</svg>

<div class="abs brand-tag">
  <svg width="133" height="128" viewBox="0 0 133 128" aria-hidden="true" style="position:absolute;left:0;top:0">
    <path d="M0 0H133V100L66.5 128L0 100Z" fill="var(--white)"/>
  </svg>
  <div class="name">Voltwise</div>
  <div class="tagline">Always switch to the cheapest energy provider</div>
</div>

<div class="abs social header-social"><span></span><span></span><span></span><span></span></div>
<nav class="abs nav">
  <span>THAT'S HOW IT WORKS</span><span>PRICES</span><span>ASK?</span><span>ABOUT US</span><span>OPERATIONS</span><span>EXPERIENCE</span><span>PRESS</span>
</nav>

<div class="abs hero-brand"><span class="name">Voltwise</span><span class="dot"></span></div>
<h1 class="abs hero-title">Always automatically switch to the cheapest energy provider</h1>
<a class="abs btn hero-btn">REGISTER NOW</a>

<svg class="abs hero-disc" viewBox="0 0 560 560" aria-hidden="true">
  <circle cx="280" cy="280" r="278" fill="var(--white)"/>
  <circle cx="280" cy="280" r="245" fill="var(--amber)"/>
</svg>

<h2 class="abs section-title known">Known from</h2>
<div class="abs press">
  <svg class="arrow" style="left:0" viewBox="0 0 16 28"><path d="M14 2L3 14L14 26" stroke="var(--amber)" stroke-width="4" fill="none"/></svg>
  <span class="badge" style="left:50px;width:125px"></span>
  <span class="badge" style="left:205px;width:140px"></span>
  <span class="badge" style="left:375px;width:70px"></span>
  <span class="badge" style="left:493px;width:105px"></span>
  <span class="badge" style="left:662px;width:90px"></span>
  <svg class="arrow" style="left:784px" viewBox="0 0 16 28"><path d="M2 2L13 14L2 26" stroke="var(--amber)" stroke-width="4" fill="none"/></svg>
</div>

<h2 class="abs section-title how">How do I become <b>Voltwise?</b></h2>

<div class="abs step-num" style="left:160px;top:960px">1</div>
<div class="abs card step" style="left:191px;top:1010px">
  <h3>Once login</h3>
  <p>upload financial statements. Select preferences. Finish the registration.</p>
</div>
<div class="abs step-num" style="left:450px;top:960px">2</div>
<div class="abs card step" style="left:482px;top:1010px">
  <h3>Automatic</h3>
  <p>fare change We pick the cheapest fare for you and carry out the change automatically.</p>
</div>
<div class="abs step-num" style="left:742px;top:955px">3</div>
<div class="abs card step" style="left:781px;top:1005px;padding-top:36px">
  <h3>Sit back and save money</h3>
  <p>Always switch automatically to the low fare.</p>
</div>

<svg class="abs portrait" viewBox="0 0 480 380" role="img" aria-label="Portrait photo of a smiling customer inside a rounded diagonal frame">
  <defs>
    <linearGradient id="portraitTone" x1="0" y1="0" x2="1" y2="1">
      <stop offset="0" stop-color="#e6d3bf"/>
      <stop offset="1" stop-color="#b58f6a"/>
    </linearGradient>
  </defs>
  <path d="M0 30L60 0H420A60 60 0 0 1 470 90V270A110 110 0 0 1 360 380H140L0 260Z" fill="#e9ebee"/>
  <path d="M140 20H400A70 70 0 0 1 470 90V270A110 110 0 0 1 360 380H250L120 120Z" fill="url(#portraitTone)"/>
</svg>

<h2 class="abs feature-title">Never pay too much for electricity &amp; gas again</h2>
<p class="abs feature-lead">Gone are the days of bad deals, tedious rate comparison and boring exchange forms.</p>
<div class="abs feature-body">
  <p>With the automatic change service for Voltwise you will never again pay too much for electricity and gas. And that, without touching a finger. We fight for you through the tariff jungle.</p>
  <p>So save your hard earned money and become a Voltwise member.</p>
</div>
<a class="abs btn feature-btn">REGISTER NOW</a>

<svg class="abs offer-bg" viewBox="0 0 1200 1041" aria-hidden="true">
  <rect x="0" y="500" width="1200" height="541" fill="var(--cream)"/>
  <path d="M0 70C300 10 800 -10 1200 40V520C900 515 300 515 0 520Z" fill="var(--orange)"/>
  <circle cx="810" cy="330" r="250" fill="none" stroke="#f57236" stroke-width="34"/>
  <circle cx="20" cy="360" r="110" fill="none" stroke="#f57236" stroke-width="26"/>
</svg>

<h2 class="abs offer-title">The cheapest of all super powers</h2>
<p class="abs offer-sub">From 24 euros you are there:</p>
<ul class="abs offer-list">
  <li>Service for electricity or gas (1 meter): 24 euros / year</li>
  <li>Service for electricity and gas (2 counters): 36 Euro / year</li>
  <li>The first fee will be charged only after your first change</li>
  <li>Save up to 850 euros annually electricity and gas costs at the first change *</li>
</ul>
<a class="abs btn offer-btn">REGISTER NOW</a>

<div class="abs device" role="img" aria-label="Smartphone showing the Voltwise app start screen"></div>

<h2 class="abs section-title save">Register once, <b>always save</b></h2>

<div class="abs card value" style="left:249px;top:2461px">
  <h3>independently</h3>
  <p>We work only for you. In order to remain independent, we consciously do without commission deals with energy providers.</p>
</div>
<div class="abs value-icon" role="img" aria-label="Paper plane icon" style="left:262px;top:2428px"></div>

<div class="abs card value" style="left:488px;top:2461px">
  <h3>automatically</h3>
  <p>You sign up once and we'll do the rest. All automatically.</p>
</div>
<div class="abs value-icon" role="img" aria-label="Gears icon" style="left:494px;top:2422px"></div>

<div class="abs card value" style="left:728px;top:2461px">
  <h3>fair</h3>
  <p>Voltwise stays more in your wallet. Despite service charge.</p>
</div>
<div class="abs value-icon" role="img" aria-label="Wallet icon" style="left:745px;top:2418px"></div>

<div class="abs footer-brand">
  <div class="name">Voltwise</div>
  <div class="tagline">Always switch to the cheapest provider</div>
</div>
<div class="abs social dark footer-social"><span></span><span></span><span></span><span></span></div>
<div class="abs footer-links">CONDITIONS<span>|</span>DATA PROTECTION<span>|</span>IMPRINT</div>

</body>
</html>
```